Halvorn Pin Keeper Brochure

We need a brochure to promote a brand new patented product. The product is a lock that ensure a shipping container itself cannot be stolen as even though you can stop someone breaking into a shipping container up until now you could not stop them from simply stealing the entire container using a crane/hyab truck/tilt tray truck/etc. This product is therefore all about security of the high value items with the container. The lock works in conjunction with standard shipping container 'twist locks'.
We would like our logo within the design. We can supply more images of required as this product is 3D modeled so you need only ask.

```html
<!DOCTYPE html>
<html lang="en">
<head>
<meta charset="utf-8">
<title>Halvorn Pin Keeper Brochure</title>
<link href="https://fonts.googleapis.com/css2?family=Dosis:wght@400;500&display=swap" rel="stylesheet">
<style>
  :root {
    --stage: #e9e7e3;
    --paper: #d9d1bc;
    --brand-red: #9a1d21;
    --on-red: #efe4d1;
    --ink: #3a3430;
    --logo-grey: #7d7d80;
  }
  * { margin: 0; padding: 0; box-sizing: border-box; }
  html, body { width: 1000px; height: 1200px; overflow: hidden; }
  body { background: var(--stage); font-family: "Dosis", sans-serif; }

  .brochure {
    position: absolute; left: 90px; top: 25px;
    width: 820px; height: 1150px;
    background: var(--paper);
    box-shadow: 0 4px 18px rgba(0,0,0,.18);
  }

  .header-band { position: absolute; left: 0; top: 34px; width: 820px; height: 92px; }

  .brand-name {
    position: absolute; left: 172px; top: 52px; width: 210px;
    text-align: center; color: var(--logo-grey);
    font-size: 34px; font-weight: 500; letter-spacing: 3px; line-height: 56px;
  }

  .intro-panel {
    position: absolute; left: 0; top: 157px; width: 544px; height: 671px;
    background: var(--brand-red); color: var(--on-red);
    padding: 55px 38px 0 38px;
    font-size: 15.3px; line-height: 19.6px; text-align: justify; hyphens: auto;
  }
  .intro-panel p + p { margin-top: 19.6px; }

  .product-renders {
    position: absolute; left: 598px; top: 157px; width: 171px;
    list-style: none;
  }
  .product-renders li { height: 98px; margin-bottom: 17px; }
  .render-a { background: linear-gradient(180deg, #b5555a 0%, #9c4a4e 60%, #a8a8a8 100%); }
  .render-b { background: linear-gradient(135deg, #a04549 0%, #c0c0c0 100%); }
  .render-c { background: linear-gradient(160deg, #6c6c6e 0%, #3c3c3e 100%); }
  .render-d { background: linear-gradient(180deg, #a84a4e 0%, #9a9a9a 55%, #c3c3c3 100%); }
  .render-e { background: linear-gradient(180deg, #4b4b4d 0%, #8a8a8c 100%); }
  .render-f { background: linear-gradient(180deg, #b85a5e 0%, #a24b4f 65%, #b0b0b0 100%); }

  .web-band {
    position: absolute; left: 0; top: 863px; width: 820px; height: 73px;
    background: var(--brand-red); color: #fff;
    text-align: center; font-size: 50px; line-height: 70px; font-weight: 400;
  }

  .offices { position: absolute; top: 986px; left: 0; width: 820px; }
  .office {
    position: absolute; top: 0;
    color: var(--ink); font-size: 14.6px; line-height: 19px; font-style: normal;
  }
  .office-sydney { left: 38px; }
  .office-perth { left: 302px; }
  .office-adelaide { left: 562px; }
</style>
</head>
<body>
  <main class="brochure">
    <svg class="header-band" viewBox="0 0 820 92" aria-hidden="true">
      <g fill="var(--brand-red)">
        <polygon points="25,0 50,0 90,46 50,92 25,92 65,46"/>
        <polygon points="60,0 85,0 118,46 85,92 60,92 93,46"/>
        <polygon points="472,0 497,0 464,46 497,92 472,92 439,46"/>
        <polygon points="507,0 820,0 820,92 507,92 474,46"/>
      </g>
    </svg>
    <div class="brand-name">VARROW</div>

    <section class="intro-panel">
      <p>Your shipping container can be easily locked securely shut, but what is stopping someone from simply picking up the entire container and stealing it with all your belongings inside? We have developed a patented locking system that allows you to easily lock your shipping container to footings or to another shipping container if you are multiple stacking.</p>
      <p>Our shipping container locks ensure your container is safe from theft by any means. It ensures your container cannot be removed from it's footings by anyone but the owner. If you need security in a shipping container yard simple use the lock to connect and lock two shipping containers together vertically. It is impossible for double stacked shipping containers to be transported due to their height even if they can be picked up!</p>
      <p>The lock is easily installed and removed in a matter of seconds, they are available individually keyed or keyed alike and are manufactured in Stainless Steel.</p>
      <p>How does it work? Our patented design works in conjunction with a standard double ended, weldable or boltable twist lock in a way that ensures the twist lock cannot be opened once the lock is installed.</p>
      <p>A minimum of two Halvorn Pin Keepers are needed per container, located in opposite corners but we advise for maximum security four should be used, one in each corner.</p>
      <p>So, the answer as to how do you stop someone stealing your shipping container is now easily answered, simply install our Halvorn Pin Keepers.</p>
    </section>

    <ul class="product-renders">
      <li class="render-a" role="img" aria-label="3D render of the lock fitted to a red container corner on its footing"></li>
      <li class="render-b" role="img" aria-label="3D render of the lock on a container corner casting, side view"></li>
      <li class="render-c" role="img" aria-label="Close-up 3D render of the lock body with its key dial and pin"></li>
      <li class="render-d" role="img" aria-label="3D render of a container corner resting on a floor grid"></li>
      <li class="render-e" role="img" aria-label="3D render of the lock mounted on a base plate"></li>
      <li class="render-f" role="img" aria-label="3D render of a red container locked down at the corner"></li>
    </ul>

    <div class="web-band">www.halvornkeeper.com.au</div>

    <div class="offices">
      <address class="office office-sydney">Sydney Office<br>52 Kestrel Ridge Rd<br>Bellmere NSW 2231<br>Tel: 0400 318 524<br>Fax: 02 9100 4417<br>info@boxwardstores.com.au</address>
      <address class="office office-perth">Perth Office<br>18 Tallow Creek Road<br>Marlow Hill WA 6071<br>Tel: (08) 9100 6382<br>perth@boxwardstores.com.au</address>
      <address class="office office-adelaide">Adelaide Office<br>41 Foundry Lane<br>Saltmere SA 5095<br>Tel: 0400 318 524<br>adelaide@boxwardstores.com.au</address>
    </div>
  </main>
</body>
</html>
```